Dental Savings Plan - Marcus Delvane DDS

We need a tri-fold brochure and 1 page flyer/poster for Dr. Marcus Delvane' dental office located on Maui, Hawaii. We are offering a new "Dental Savings Plan" to patients.
I have included 3 photos, along with the office logo. You do not have to use all photos if you do not want to. We want this to catch the eyes of patients, easy for them to read and understand, and to show them that this is a much better option than dental insurance.
Please use same Hawaiian theme and colors on the office website https://www.pearlreefcare.com .

Please also include the following to promote this new plan:

Dental Services Include
• Professional Dental Cleanings (2 per benefit year)
• Perio Maintenance Cleanings (3 per benefit year) covered at 80%
• Radiographs as needed (1 set of X-rays per benefit year)
• Doctor Examinations (2 per benefit year)
• Ozone Treatment
• KOROV Amalgam Removal
• Additional limited/emergency exam (1 per benefit year)
• Cosmetic consultation
• 15% discount on all other services (including cosmetic procedures)
• 10% discount on implants and implant crowns

Advantages of the Dental Savings Plan
1. No deductibles
2. No waiting periods
3. No claims to file
4. No frequency limitations or exclusions
5. No yearly maximum benefits
6. No pre-authorization requirements
7. No pre-existing conditions limitations
8. State of the art facility and technology
9. Immediate enrollment
10. Highest quality of care for you and your Ohana

Annual Fee
$399 first family member/individual (equivalent to $33 per month)
$349 second family member (equivalent to $29 per month)
$249 each additional family member (equivalent to $20 per month)

Provisions of the Dental Savings Plan
• May not be combined with insurance plans, discounts or promotions
• This Dental Savings Plan is not an insurance plan, but a payment arrangement provided by Marcus Delvane DDS, and is not transferable to any other dental office or dental specialist
• Payment for services are due at the date of service
• This program is for you and is not transferable
• Benefits are provided for one year from the date the plan is purchased
• Must be paid in full when starting the plan
• No refunds will be provided for dues of the plan annual fee under any circumstances, including failure to schedule and maintain appointments
• If Paxwel Fund is used to pay for the program and for services then only a 10% discount will be given
• To receive the full 15% discount on restorative treatment, you must schedule the appointment the day it is recommended. Any failed appointment results in the loss of the 15% discount.

Target Market(s)

Dental patients without dental insurance

Industry/Entity Type

Dental Clinic

Requirements
Must have
• My project must have the logo file to identify the dental office, Hawaiian theme, same colors as website, match style of website font, theme and colors, as well as, all the Dental Services, Advantages of the Dental Savings Plan, Annual Fee, and the Provisions of the Dental Savings Plan.

```html
<!DOCTYPE html>
<html lang="en">
<head>
<meta charset="utf-8">
<title>Dental Savings Plan – Marcus Delvane DDS</title>
<link href="https://fonts.googleapis.com/css2?family=Libre+Baskerville:wght@700&family=Open+Sans:wght@400;600;700&display=swap" rel="stylesheet">
<style>
:root{
  --bg:#5e5e5e;
  --blue:#1e9fd9;
  --blue-deep:#1488c4;
  --green:#7cc242;
  --ink:#3d4a55;
  --sky-top:#e3f3fb;
  --sky-bottom:#cfe9f5;
  --white:#ffffff;
}
*{margin:0;padding:0;box-sizing:border-box}
html,body{width:960px;height:1200px;overflow:hidden;background:var(--bg)}
body{position:relative;font-family:'Open Sans',sans-serif;color:var(--ink)}
.sheet{position:absolute;left:97px;width:742px;height:526px;overflow:hidden;
  background:linear-gradient(180deg,var(--sky-top) 0%,var(--sky-bottom) 100%)}
.sheet--outside{top:60px}
.sheet--inside{top:610px}
.wave{position:absolute;left:0;top:0;width:742px;height:526px}
.panel{position:absolute;top:0;width:247px;height:526px}
.panel--left{left:0}
.panel--mid{left:247px;border-left:1px solid rgba(255,255,255,.35)}
.panel--right{left:494px;border-left:1px solid rgba(255,255,255,.35)}
.serif{font-family:'Libre Baskerville',serif;font-weight:700;text-transform:uppercase}
.tab{position:absolute;color:var(--white);text-align:center;border-radius:0 0 14px 14px;
  display:flex;align-items:center;justify-content:center;line-height:1}
.tab--green{background:var(--green)}
.tab--blue{background:var(--blue)}
.photo{position:absolute;background:linear-gradient(135deg,#f3d9c9,#bcd9ea)}
.photo--circle{border-radius:50%;border:4px solid var(--green)}
.map{position:absolute;border-radius:50%;border:4px solid var(--green);
  background:linear-gradient(135deg,#f4f4f2,#e6e9ec)}
/* fees */
.fee{position:absolute;left:20px;width:220px}
.fee__row{display:flex;align-items:center;gap:4px}
.fee__price{background:var(--blue);color:var(--white);font-family:'Libre Baskerville',serif;font-weight:700;
  font-size:26px;line-height:32px;padding:0 3px;border-radius:2px}
.fee__label{font-size:13px;font-weight:600;line-height:13px;text-transform:uppercase;color:#33404a}
.fee__note{font-size:15px;margin-top:4px;color:#3a4650}
.fee__rule{position:absolute;left:20px;width:210px;height:1px;background:var(--green);opacity:.7}
/* contact */
.contact{position:absolute;left:0;width:247px;text-align:center;font-size:13px;line-height:15px;color:#34414c}
.icon{display:block;margin:0 auto}
.cta{position:absolute;left:0;width:247px;text-align:center;color:var(--white);font-size:16px;line-height:20px;font-weight:600;text-transform:uppercase}
.social{position:absolute;left:0;width:247px;top:488px;display:flex;justify-content:center;gap:6px}
.social span{width:24px;height:24px;border-radius:50%;background:var(--white)}
.brand{position:absolute;left:0;top:30px;width:247px;text-align:center}
.brand__dot{width:54px;height:54px;border-radius:50%;background:var(--green);margin:0 auto 10px}
.brand__name{font-size:14px;font-weight:600;color:var(--blue-deep);text-transform:uppercase;letter-spacing:.5px}
.headline{position:absolute;left:0;top:472px;width:247px;text-align:center;color:var(--white);font-size:25px;line-height:28px}
/* lists */
.list{position:absolute;list-style:none}
.list li{position:relative;padding-left:14px;font-size:10.5px;line-height:12px;color:#3f4b55}
.list li::before{content:"✓";position:absolute;left:0;top:0;color:var(--blue);font-weight:700}
.list--services{left:18px;top:86px;width:222px}
.list--services li{margin-bottom:7px}
.list--adv{left:40px;top:86px;width:206px}
.list--adv li{font-size:11px;margin-bottom:11px;white-space:nowrap}
.list--plus{left:20px;top:260px;width:220px}
.list--plus li{font-size:11px;margin-bottom:8px}
.list--prov{left:16px;top:82px;width:226px}
.list--prov li{font-size:9.8px;line-height:11px;margin-bottom:6px}
.no-mark{position:absolute;left:18px;top:84px;width:20px;height:162px;display:flex;align-items:center;justify-content:center}
.no-mark::before{content:"";position:absolute;left:9px;top:0;width:2px;height:100%;background:var(--green)}
.no-mark span{position:relative;background:var(--sky-top);color:var(--green);font-weight:700;font-size:20px;
  transform:rotate(-90deg);padding:4px 0}
</style>
</head>
<body>

<section class="sheet sheet--outside">
  <svg class="wave" viewBox="0 0 742 526" aria-hidden="true">
    <path d="M0,412 C140,370 300,340 460,392 S650,430 742,378 L742,526 L0,526 Z" fill="var(--green)"/>
    <path d="M0,424 C140,384 300,356 460,406 S650,444 742,392 L742,526 L0,526 Z" fill="var(--blue)"/>
  </svg>

  <div class="panel panel--left">
    <div class="tab tab--green serif" style="left:42px;top:0;width:164px;height:40px;font-size:19px">Annual Fee</div>

    <div class="fee" style="top:70px">
      <div class="fee__row"><span class="fee__price">$399</span><span class="fee__label">First family<br>member/individual</span></div>
      <p class="fee__note">(equivalent to $33 per month)</p>
    </div>
    <div class="fee__rule" style="top:132px"></div>
    <div class="fee" style="top:142px">
      <div class="fee__row"><span class="fee__price">$349</span><span class="fee__label">Second family<br>member</span></div>
      <p class="fee__note">(equivalent to $29 per month)</p>
    </div>
    <div class="fee__rule" style="top:204px"></div>
    <div class="fee" style="top:214px">
      <div class="fee__row"><span class="fee__price">$249</span><span class="fee__label">Each additional<br>family member</span></div>
      <p class="fee__note">(equivalent to $20 per month)</p>
    </div>

    <div class="photo photo--circle" style="left:39px;top:304px;width:148px;height:148px" role="img" aria-label="Close-up photo of a smiling patient during a dental check-up"></div>

    <p class="cta" style="top:468px;font-size:14px">Follow us on</p>
    <div class="social" aria-label="Social media links">
      <span></span><span></span><span></span><span></span><span></span><span></span>
    </div>
  </div>

  <div class="panel panel--mid">
    <div class="map" style="left:44px;top:30px;width:160px;height:160px" role="img" aria-label="Street map showing the office location"></div>

    <div class="contact" style="top:214px">
      <svg class="icon" width="14" height="18" viewBox="0 0 14 18"><path d="M7 0C3.1 0 0 3.1 0 7c0 5 7 11 7 11s7-6 7-11c0-3.9-3.1-7-7-7zm0 9.5A2.5 2.5 0 1 1 7 4.5a2.5 2.5 0 0 1 0 5z" fill="var(--green)"/></svg>
      <p style="margin-top:8px">742 Palm Lagoon Rd # 18<br>Kihei, HI 96753</p>
    </div>
    <div class="contact" style="top:279px">
      <svg class="icon" width="16" height="12" viewBox="0 0 16 12"><path d="M2 3C2 1 4 0 8 0s6 1 6 3v1h-3V2.5H5V4H2zM3 5h10l2 6H1z" fill="var(--green)"/></svg>
      <p style="margin-top:6px;font-size:15px">808-555-0142</p>
    </div>
    <div class="contact" style="top:326px">
      <svg class="icon" width="14" height="14" viewBox="0 0 14 14"><circle cx="7" cy="7" r="6" fill="none" stroke="var(--green)" stroke-width="1.6"/><path d="M1 7h12M7 1c-3 3-3 9 0 12M7 1c3 3 3 9 0 12" fill="none" stroke="var(--green)" stroke-width="1.2"/></svg>
      <p style="margin-top:5px;font-size:15px">www.pearlreefcare.com</p>
    </div>

    <p class="cta" style="top:466px">Book an appointment<br>We love new patients!</p>
  </div>

  <div class="panel panel--right" style="background:linear-gradient(180deg,var(--white) 0%,var(--white) 22%,transparent 22%)">
    <div class="brand">
      <div class="brand__dot"></div>
      <p class="brand__name">Marcus Delvane DDS</p>
    </div>
    <div class="photo" style="left:0;top:120px;width:247px;height:300px" role="img" aria-label="Photo of a dentist treating a patient in the dental chair"></div>
    <h1 class="headline serif">Dental<br>Savings Plan</h1>
  </div>
</section>

<section class="sheet sheet--inside">
  <svg class="wave" viewBox="0 0 742 526" aria-hidden="true">
    <path d="M0,414 C160,370 300,366 440,392 S640,420 742,382 L742,526 L0,526 Z" fill="var(--green)"/>
    <path d="M0,426 C160,384 300,380 440,406 S640,434 742,396 L742,526 L0,526 Z" fill="var(--blue)"/>
  </svg>

  <div class="panel panel--left">
    <div class="tab tab--green serif" style="left:42px;top:0;width:164px;height:62px;font-size:22px;line-height:22px">Dental<br>Services</div>
    <ul class="list list--services">
      <li>Professional Dental Cleanings<br>(2 per benefit year)</li>
      <li>Perio Maintenance Cleanings<br>(3 per benefit year) covered at 80%</li>
      <li>Radiographs as needed (1 set of X-rays per benefit year)</li>
      <li>Doctor Examinations (2 per benefit year)</li>
      <li>Ozone Treatment</li>
      <li>KOROV Amalgam Removal</li>
      <li>Additional limited/emergency exam<br>(1 per benefit year)</li>
      <li>Cosmetic consultation</li>
      <li>15% discount on all other services (including cosmetic procedures)</li>
      <li>10% discount on implants and implant crowns</li>
    </ul>
    <p class="cta" style="top:467px">Book an appointment<br>We love new patients!</p>
  </div>

  <div class="panel panel--mid">
    <div class="tab tab--blue serif" style="left:20px;top:0;width:208px;height:48px;font-size:14px;line-height:14px">Advantages of the<br>Dental Savings Plan</div>
    <div class="no-mark"><span>NO</span></div>
    <ul class="list list--adv">
      <li>deductibles</li>
      <li>waiting periods</li>
      <li>claims to file</li>
      <li>frequency limitations or exclusions</li>
      <li>yearly maximum benefits</li>
      <li>pre-authorization requirements</li>
      <li>pre-existing conditions limitations</li>
    </ul>
    <ul class="list list--plus">
      <li>State of the art facility and technology</li>
      <li>Immediate enrollment</li>
      <li>Highest quality of care for you and your Ohana</li>
    </ul>
    <div class="photo photo--circle" style="left:58px;top:330px;width:126px;height:126px" role="img" aria-label="Close-up photo of a smiling patient during a dental check-up"></div>
    <p class="cta" style="top:483px;font-size:15px;text-transform:none;font-weight:400">www.pearlreefcare.com</p>
  </div>

  <div class="panel panel--right">
    <div class="tab tab--green serif" style="left:20px;top:0;width:208px;height:48px;font-size:14px;line-height:14px">Provisions of the<br>Dental Savings Plan</div>
    <ul class="list list--prov">
      <li>May not be combined with insurance plans, discounts or promotions</li>
      <li>This Dental Savings Plan is not an insurance plan, but a payment arrangement provided by Marcus Delvane DDS, and is not transferable to any other dental office or dental specialist</li>
      <li>Payment for services are due at the date of service</li>
      <li>This program is for you and is not transferable</li>
      <li>Benefits are provided for one year from the date the plan is purchased</li>
      <li>Must be paid in full when starting the plan</li>
      <li>No refunds will be provided for dues of the plan annual fee under any circumstances, including failure to schedule and maintain appointments</li>
      <li>If Paxwel Fund is used to pay for the program and for services then only a 10% discount will be given</li>
      <li>To receive the full 15% discount on restorative treatment, you must schedule the appointment the day it is recommended. Any failed appointment results in the loss of the 15% discount.</li>
    </ul>
    <p class="cta" style="top:474px;font-size:15px;font-weight:700">We want to be your Kihei<br>&amp; Wailea dentist!</p>
  </div>
</section>

</body>
</html>
```